Lobo Taqueria Car Show Flyer

Looking for a creative flyer to send digitally to invite car enthusiast all over to an event at a Restaurant. Uploading to Socials like Pixa, Chatterly, ETC. Must incorporate the restuarant hosting www.lobotaqueria-demo.com (feel free to use any logos or photos on the site. Also need the Dremix logo. A few choices attached. And finally the VXL should be prominently placed. One idea is to incorporate the restaurant in the background. but i'm open to all creative. A coworker drafted something with AI (attached)and that's just yuck. So here I am trusting the real creatives. Event Date: Sunday, Oct 26th. , Address: 4172 Halvard Pinecrest Rd, Orlando, FL 32999

Target Market(s)

Would like to appeal to JDM and Classic Car Crowd

Requirements
Must have
• Date, Location, Lobo Taqueria Logo or Mascot, Dremix logo

```html
<!DOCTYPE html>
<html lang="en">
<head>
<meta charset="utf-8">
<title>Lobo Taqueria Car Show Flyer</title>
<link href="https://fonts.googleapis.com/css2?family=Bebas+Neue&family=Poppins:wght@500;600&display=swap" rel="stylesheet">
<style>
  :root {
    --stage: #a3a3a3;
    --paper: #f4f4f4;
    --red-deep: #6e0008;
    --red-mid: #a3141b;
    --red-warm: #c9452e;
    --badge-red: #a80a0f;
    --white: #ffffff;
    --ink: #161616;
    --car-light: #b9bcaa;
    --car-dark: #6f7264;
  }
  * { margin: 0; padding: 0; box-sizing: border-box; }
  html, body { width: 869px; height: 1200px; overflow: hidden; background: var(--stage); }
  .canvas { position: relative; width: 869px; height: 1200px; background: var(--stage); }
  .flyer {
    position: absolute; left: 96px; top: 93px; width: 677px; height: 1014px;
    background: var(--paper); overflow: hidden;
  }
  .hero-panel {
    position: absolute; left: 57px; top: 0; width: 563px; height: 650px;
    border-radius: 0 0 282px 282px / 0 0 300px 300px;
    background: linear-gradient(180deg, var(--red-deep) 0%, var(--red-mid) 40%, var(--red-warm) 68%, var(--red-mid) 100%);
  }
  .headline { position: absolute; left: 57px; width: 563px; text-align: center; color: var(--white);
    font-family: 'Bebas Neue', sans-serif; font-weight: 400; line-height: 1; white-space: nowrap; }
  .presenters { top: 26px; font-size: 30px; }
  .invite { top: 90px; font-size: 72px; }
  .invite-big { top: 151px; font-size: 244px; -webkit-text-stroke: 4px var(--white); letter-spacing: 2px; }
  .invite-sub { top: 360px; font-size: 64px; letter-spacing: 1.5px; }
  .car-photo {
    position: absolute; left: 43px; top: 444px; width: 594px; height: 352px;
    border-radius: 45% 40% 30% 35% / 50% 45% 35% 40%;
    background: linear-gradient(160deg, var(--car-light) 0%, #9ea190 45%, var(--car-dark) 100%);
  }
  .date-badge {
    position: absolute; z-index: 2; left: 20px; top: 682px; width: 204px; height: 204px; border-radius: 50%;
    background: var(--badge-red); color: var(--white); font-family: 'Bebas Neue', sans-serif;
  }
  .date-day { position: absolute; left: 51px; top: 27px; font-size: 44px; line-height: 1; }
  .date-num { position: absolute; left: 51px; top: 66px; font-size: 83px; line-height: 1; }
  .date-num sup { font-size: 42px; position: relative; top: -34px; vertical-align: baseline; }
  .date-month { position: absolute; left: 51px; top: 140px; font-size: 43px; line-height: 1; }
  .location { position: absolute; left: 252px; top: 806px; display: flex; align-items: center; }
  .location-pin { width: 21px; height: 29px; }
  .location-rule { width: 1px; height: 48px; background: var(--ink); margin: 0 18px 0 12px; }
  .location-address { font-family: 'Poppins', sans-serif; font-weight: 500; font-size: 21px;
    line-height: 27.5px; color: var(--ink); white-space: nowrap; }
  .host-mark {
    position: absolute; z-index: 1; left: 40px; top: 878px; width: 158px; height: 136px; background: var(--white);
    display: flex; align-items: flex-end; justify-content: center; gap: 7px; padding-bottom: 22px;
    font-family: 'Bebas Neue', sans-serif; font-size: 25px; line-height: 1; color: var(--badge-red);
  }
  .host-mark .dot { width: 14px; height: 14px; border-radius: 50%; background: var(--badge-red); margin-bottom: 4px; }
  .partner-mark {
    position: absolute; left: 265px; top: 919px; width: 164px; height: 72px;
    display: flex; align-items: center; justify-content: center; gap: 8px;
    font-family: 'Bebas Neue', sans-serif; font-size: 34px; color: var(--ink);
  }
  .partner-mark .square { width: 14px; height: 14px; background: var(--ink); }
  .mascot {
    position: absolute; left: 496px; top: 851px; width: 141px; height: 163px;
    border-radius: 60px 60px 6px 6px;
    background: linear-gradient(180deg, #4a2a1e 0%, #b5652d 45%, #c4531f 70%, #2f4a35 100%);
  }
</style>
</head>
<body>
<div class="canvas">
  <section class="flyer">
    <div class="hero-panel" role="img" aria-label="Red-tinted photo of the Lobo Taqueria restaurant building and its parking lot"></div>
    <p class="headline presenters">Lobo Taqueria &amp; Dremix Vintage Collection Presnt</p>
    <h1 class="headline invite">Inviting All</h1>
    <p class="headline invite-big">Car</p>
    <p class="headline invite-sub">Enthusiasts!</p>
    <div class="car-photo" role="img" aria-label="Photo of a gray-green VXL sports coupe with bronze wheels"></div>
    <div class="host-mark"><span class="dot"></span>Lobo Taqueria</div>
    <div class="date-badge">
      <span class="date-day">Sunday</span>
      <span class="date-num">26<sup>th</sup></span>
      <span class="date-month">October</span>
    </div>
    <div class="location">
      <svg class="location-pin" viewBox="0 0 22 30" aria-hidden="true">
        <path d="M11 0C5 0 0 4.8 0 10.8 0 18 11 30 11 30s11-12 11-19.2C22 4.8 17 0 11 0z" fill="#b0131a"/>
        <circle cx="11" cy="10.5" r="4" fill="#fff"/>
      </svg>
      <span class="location-rule"></span>
      <p class="location-address">4172 Halvard Pinecrest Rd,<br>Orlando, FL 32999</p>
    </div>
    <div class="partner-mark"><span class="square"></span>Dremix</div>
    <div class="mascot" role="img" aria-label="Illustrated restaurant mascot in a flowered hat and tropical print jacket"></div>
  </section>
</div>
</body>
</html>
```